Tea box package for Herbal Teas

We would like a design for a package of our tea products. We want the consumer to understand that our products are natural just by looking at the package. We prefer minimalistic designs.
The package we want would be a square (or slightly rectangular) box. The box would be generic enough for us to use it for different teas. Essentially what we want is all the main information and designs to be the same for each tea product we have. We would like to be able to change the main color and the name of the tea then to customize to the tea in the package. Please see the attached images for examples.
We really like the package in tea_packaging_example_4 picture. We would like our packaging to be something very similar but with all the labels printed on the package.
We already have our logo so I am attaching that as well (image named 'velka brin logo copy'). That would go on the front of the box.
We also attach a tile created using our logo (see image called 'tile'). We would like this to go to the sides similarly to tea_packaging_example_4.
On the back of the pouch, we want to have directions on how to make the tea but we want this section to be editable. For now just 3-4 lines of sample text is fine along with instructions on how to make a tea, see picture 'back of tea box'.
We would like for the box color to be as in example picture
tea_packaging_example_4. The color of the writing should be the same as the logo color. The font style should be something that would look nice next to the logo font, we are not sure what that font should be. The only thing colored would be the name of the tea and the ribbon as seen in tea_packaging_example_4, which we would like to change if we need to, to other variations.
Thanks a lot. For any questions, please contact me.

```html
<!DOCTYPE html>
<html lang="en">
<head>
<meta charset="utf-8">
<title>Velka Brin – Silver Tips White Tea box dieline</title>
<link href="https://fonts.googleapis.com/css2?family=Tinos:wght@400;700&display=swap" rel="stylesheet">
<style>
  :root {
    --ink: #3a3a3a;
    --tea-green: #136b4a;
    --paper: #ffffff;
    --cut-line: #1a1a1a;
  }
  html, body {
    margin: 0;
    padding: 0;
    width: 1200px;
    height: 1200px;
    overflow: hidden;
    background: var(--paper);
  }
  .dieline {
    position: relative;
    width: 1200px;
    height: 1200px;
    font-family: "Tinos", "Times New Roman", serif;
  }
  .dieline svg {
    position: absolute;
    inset: 0;
    width: 1200px;
    height: 1200px;
  }
  .cut { fill: none; stroke: var(--cut-line); stroke-width: 1.2; }
  .panel-border { fill: none; stroke: var(--ink); stroke-width: 10; stroke-dasharray: 26 14; }
  .corner { fill: var(--ink); }
  .ink-fill { fill: var(--ink); }
  .green-fill { fill: var(--tea-green); }
  .paper-fill { fill: var(--paper); }
  .brand-name { font-family: "Tinos", "Times New Roman", serif; fill: var(--ink); font-size: 15px; letter-spacing: 0.5px; }
  .tea-sub { font-family: "Tinos", "Times New Roman", serif; fill: var(--paper); font-size: 9.5px; }
  .tea-name { font-family: "Tinos", "Times New Roman", serif; fill: var(--paper); font-size: 16px; letter-spacing: 0.5px; }

  .back-copy {
    position: absolute;
    left: 623px;
    top: 566px;
    width: 148px;
    color: var(--ink);
    font-size: 6.8px;
    line-height: 8.9px;
    text-align: justify;
    text-align-last: center;
  }
  .back-copy p { margin: 0 0 8.9px; }
  .back-copy .back-title { display: block; text-align: center; }
</style>
</head>
<body>
<div class="dieline">
  <svg viewBox="0 0 1500 1500" xmlns="http://www.w3.org/2000/svg">
    <polygon class="cut" points="1327,660 1358,673 1358,938 1327,960"/>
    <path class="cut" d="M726,358 L726,660 H720 Q679,660 679,614 V404 Q679,358 726,358 Z"/>
    <path class="cut" d="M1027,358 Q1073,358 1073,404 V614 Q1073,660 1027,660 Z"/>
    <path class="cut" d="M824,358 V330 Q824,308 846,308 H907 Q929,308 929,330 V358"/>
    <polyline class="cut" points="124,960 202,1080 202,1122 346,1122 346,1080 425,960"/>
    <polyline class="cut" points="425,960 425,1122 526,1122 526,1076 726,960"/>
    <polyline class="cut" points="726,960 726,1122 803,1122 803,1080 948,1080 948,1122 1027,1122 1027,960"/>
    <polyline class="cut" points="1027,960 1225,1076 1225,1122 1327,1122 1327,960"/>

    <g class="frames">
      <rect class="panel-border" x="129" y="665" width="291" height="290"/>
      <rect class="panel-border" x="430" y="665" width="291" height="290"/>
      <rect class="panel-border" x="731" y="665" width="291" height="290"/>
      <rect class="panel-border" x="1032" y="665" width="290" height="290"/>
      <rect class="panel-border" x="731" y="363" width="291" height="292"/>
      <g class="corner">
        <rect x="124" y="660" width="44" height="14"/><rect x="124" y="660" width="14" height="44"/>
        <rect x="124" y="946" width="44" height="14"/><rect x="124" y="916" width="14" height="44"/>
        <rect x="381" y="660" width="88" height="14"/><rect x="411" y="660" width="28" height="44"/>
        <rect x="381" y="946" width="88" height="14"/><rect x="411" y="916" width="28" height="44"/>
        <rect x="682" y="660" width="88" height="14"/><rect x="712" y="660" width="28" height="44"/>
        <rect x="682" y="946" width="88" height="14"/><rect x="712" y="916" width="28" height="44"/>
        <rect x="983" y="660" width="88" height="14"/><rect x="1013" y="660" width="28" height="44"/>
        <rect x="983" y="946" width="88" height="14"/><rect x="1013" y="916" width="28" height="44"/>
        <rect x="1283" y="660" width="44" height="14"/><rect x="1313" y="660" width="14" height="44"/>
        <rect x="1283" y="946" width="44" height="14"/><rect x="1313" y="916" width="14" height="44"/>
        <rect x="726" y="358" width="44" height="14"/><rect x="726" y="358" width="14" height="44"/>
        <rect x="983" y="358" width="44" height="14"/><rect x="1013" y="358" width="14" height="44"/>
        <rect x="726" y="646" width="44" height="14"/><rect x="726" y="616" width="14" height="44"/>
        <rect x="983" y="646" width="44" height="14"/><rect x="1013" y="616" width="14" height="44"/>
      </g>
    </g>

    <g class="front-panel">
      <rect class="ink-fill" x="173" y="708" width="203" height="204" rx="20" role="img" aria-label="Ornamental tile pattern frame"/>
      <path class="green-fill" d="M207,660 H246 A29,29 0 0 0 304,660 H342 V708 H207 Z"/>
      <rect class="paper-fill" x="207" y="710" width="135" height="102"/>
      <circle class="ink-fill" cx="275" cy="752" r="9"/>
      <text class="brand-name" x="275" y="800" text-anchor="middle">VELKA BRIN</text>
      <path class="green-fill" d="M204,813 H346 V822 Q346,891 275,891 Q204,891 204,822 Z" stroke="#ffffff" stroke-width="3"/>
      <text class="tea-sub" x="275" y="835" text-anchor="middle">SILVER TIPS</text>
      <text class="tea-name" x="275" y="850" text-anchor="middle">WHITE TEA</text>
    </g>

    <rect class="ink-fill" x="502" y="737" width="146" height="146" rx="22" transform="rotate(45 575 810)" role="img" aria-label="Ornamental tile pattern"/>
    <rect class="ink-fill" x="1104" y="737" width="146" height="146" rx="22" transform="rotate(45 1177 810)" role="img" aria-label="Ornamental tile pattern"/>

    <g class="lid-panel">
      <rect class="green-fill" x="808" y="358" width="135" height="50"/>
      <rect class="ink-fill" x="808" y="407" width="135" height="3"/>
      <rect class="ink-fill" x="808" y="511" width="135" height="3"/>
      <circle class="ink-fill" cx="876" cy="472" r="9"/>
      <text class="brand-name" x="876" y="427" text-anchor="middle" transform="rotate(180 876 422)">VELKA BRIN</text>
      <path class="green-fill" d="M808,516 H943 V520 Q943,588 876,588 Q808,588 808,520 Z"/>
    </g>
  </svg>

  <div class="back-copy">
    <p class="back-title">Silver Tips White Tea</p>
    <p><span class="back-title">What’s special about this tea?</span>Grow in the Fujian province of china, tea buds are plucked within two hours of sprouting, then withered naurally in the sun. If your usual white tea appears green in your cup, then it is green tea; this, however, is the genuine article. Possibly one of our most exclusive teas - refreshing, light and aromatic.</p>
    <p><span class="back-title">Our leaf lanterns:</span>We use quality whole leaf only, not the dust found in regular tea bags; whole leaf is best. a tea worthy of worship belongs in our biodegradable “leaf lantern” - our spacious, transparent mesh bag allowing maximum room for perfect infusion.</p>
  </div>
</div>
</body>
</html>
```